Need Eye Catching For Sale By Owner Signs

In need of a Eye Catching For Sale By Owner Sign design. I plan on using the sign to market buildings and raw land that I own. The design should be able to scale to different rectangular dimensions for example a yard stake sign or a large 4' x 6' sign to be tacked to plywood. The design should have a dead space near the bottom that I can insert more detail information into at a later time.

The main tag line "For Sale By Owner" and the contact number "318-562-4097" needs to be easily be read from a distance.

```html
<!DOCTYPE html>
<html lang="en">
<head>
<meta charset="utf-8">
<title>For Sale By Owner Sign</title>
<link rel="stylesheet" href="https://fonts.googleapis.com/css2?family=Anton&display=swap">
<style>
  :root {
    --sign-red: #ec1c24;
    --headline-white: #ffffff;
    --contact-black: #000000;
    --page-white: #ffffff;
  }
  html, body {
    margin: 0;
    padding: 0;
    width: 1200px;
    height: 800px;
    overflow: hidden;
    background: var(--page-white);
  }
  .sign {
    position: relative;
    width: 1200px;
    height: 800px;
    font-family: "Anton", Impact, sans-serif;
  }
  .sign-shape {
    position: absolute;
    inset: 0;
  }
  .sign-headline,
  .sign-contact-label,
  .sign-contact-number {
    position: absolute;
    left: 50px;
    margin: 0;
    white-space: nowrap;
    line-height: 1;
    font-weight: 400;
  }
  .sign-headline {
    top: 138px;
    font-size: 144px;
    letter-spacing: 2px;
    color: var(--headline-white);
  }
  .sign-contact-label {
    top: 336px;
    font-size: 120px;
    letter-spacing: 4px;
    color: var(--contact-black);
  }
  .sign-contact-number {
    top: 496px;
    font-size: 122px;
    letter-spacing: 4px;
    color: var(--contact-black);
  }
</style>
</head>
<body>
  <main class="sign">
    <svg class="sign-shape" width="1200" height="800" viewBox="0 0 1200 800" aria-hidden="true">
      <defs>
        <pattern id="teeth-top" x="0" y="0" width="25" height="14" patternUnits="userSpaceOnUse">
          <polygon points="0,14 12.5,0 25,14" fill="var(--sign-red)"/>
        </pattern>
        <pattern id="teeth-bottom" x="0" y="786" width="25" height="14" patternUnits="userSpaceOnUse">
          <polygon points="0,0 12.5,14 25,0" fill="var(--sign-red)"/>
        </pattern>
        <pattern id="teeth-left" x="0" y="0" width="14" height="25" patternUnits="userSpaceOnUse">
          <polygon points="14,0 0,12.5 14,25" fill="var(--sign-red)"/>
        </pattern>
        <pattern id="teeth-right" x="1186" y="0" width="14" height="25" patternUnits="userSpaceOnUse">
          <polygon points="0,0 14,12.5 0,25" fill="var(--sign-red)"/>
        </pattern>
      </defs>
      <rect x="14" y="14" width="1172" height="772" fill="var(--sign-red)"/>
      <rect x="14" y="0" width="1172" height="14" fill="url(#teeth-top)"/>
      <rect x="14" y="786" width="1172" height="14" fill="url(#teeth-bottom)"/>
      <rect x="0" y="14" width="14" height="772" fill="url(#teeth-left)"/>
      <rect x="1186" y="14" width="14" height="772" fill="url(#teeth-right)"/>
    </svg>
    <h1 class="sign-headline">For Sale By Owner</h1>
    <p class="sign-contact-label">Contact number:</p>
    <p class="sign-contact-number">318-562-4097</p>
  </main>
</body>
</html>
```